Tallow Crest Business Card

We need a business card designed for a a company called "Tallow Crest". We offer consulting, coaching and training to business leaders and coaches (across the world) using the latest findings in neuroscience, social and emotional intelligence and positive psychology. The final design should communicate the use of brain science to create sustainable relationships.

The card should be doublesided. The logo is attached and names and titles will be provided to the successful designer. Thank you.

Industry/Entity Type

Training

```html
<!DOCTYPE html>
<html lang="en">
<head>
<meta charset="utf-8">
<title>Tallow Crest Business Card</title>
<link rel="stylesheet" href="https://fonts.googleapis.com/css2?family=Roboto:wght@300;400;700&display=swap">
<style>
  :root {
    --brand-blue: #0f8dc4;
    --brand-lime: #bfd730;
    --stage-light: #f4f4f4;
    --stage-dark: #9c9c9c;
    --card-face: #efefef;
    --card-glow: #fbfbfb;
    --card-edge: #ffffff;
    --ink-dark: #1e1e1e;
    --ink-mid: #8a8a8a;
    --ink-label: #7a7a7a;
  }
  * { box-sizing: border-box; margin: 0; padding: 0; }
  html, body {
    width: 1200px;
    height: 1000px;
    overflow: hidden;
  }
  body {
    position: relative;
    font-family: "Roboto", Arial, sans-serif;
    background: linear-gradient(150deg, var(--stage-light) 0%, #d9d9d9 50%, var(--stage-dark) 100%);
  }

  .card {
    position: absolute;
    top: 220px;
    width: 310px;
    height: 560px;
    box-shadow: 0 10px 24px rgba(0, 0, 0, 0.18);
  }

  /* Front side */
  .card--front {
    left: 250px;
    padding: 7px;
    background: linear-gradient(to bottom, var(--brand-blue) 0 56%, var(--brand-lime) 56% 100%);
  }
  .card--front .card__face {
    width: 100%;
    height: 100%;
    background: radial-gradient(circle at 50% 40%, var(--card-glow) 0%, #eeeeee 55%, #e2e2e2 100%);
    display: flex;
    flex-direction: column;
    align-items: center;
    justify-content: center;
    gap: 26px;
  }
  .brand-dot {
    width: 92px;
    height: 92px;
    border-radius: 50%;
    background: var(--brand-lime);
  }
  .brand-name {
    font-weight: 700;
    font-size: 40px;
    line-height: 1.05;
    color: var(--brand-blue);
    text-align: center;
    letter-spacing: 0.5px;
  }

  /* Back side */
  .card--back {
    left: 640px;
    padding: 9px;
    background: var(--card-edge);
  }
  .card--back .card__face {
    position: relative;
    width: 100%;
    height: 100%;
    background: var(--card-face);
    text-align: center;
    overflow: hidden;
  }
  .person {
    padding-top: 78px;
  }
  .person__name {
    font-weight: 400;
    font-size: 31px;
    color: var(--ink-dark);
  }
  .person__title {
    font-weight: 300;
    font-size: 18px;
    color: var(--ink-mid);
    margin-top: 2px;
  }
  .contact {
    position: absolute;
    top: 290px;
    left: 0;
    right: 0;
    font-size: 16px;
    line-height: 22px;
    color: var(--ink-mid);
    font-weight: 300;
  }
  .contact__label {
    font-weight: 700;
    color: var(--ink-label);
  }
  .contact__web {
    margin-top: 12px;
    color: var(--brand-blue);
    font-weight: 400;
  }
  .back-mark {
    position: absolute;
    left: 0;
    right: 0;
    bottom: 40px;
    font-weight: 700;
    font-size: 44px;
    line-height: 1.05;
    color: rgba(255, 255, 255, 0.75);
  }
</style>
</head>
<body>
  <section class="card card--front" aria-label="Card front">
    <div class="card__face">
      <div class="brand-dot"></div>
      <div class="brand-name">Tallow<br>Crest</div>
    </div>
  </section>

  <section class="card card--back" aria-label="Card back">
    <div class="card__face">
      <div class="person">
        <div class="person__name">Maren Holt</div>
        <div class="person__title">Director</div>
      </div>
      <div class="contact">
        <div><span class="contact__label">PH:</span> 555 210 48 73</div>
        <div><span class="contact__label">MAIL:</span> hello@tallowcrest.com</div>
        <div class="contact__web">www.tallowcrest.com</div>
      </div>
      <div class="back-mark">Tallow<br>Crest</div>
    </div>
  </section>
</body>
</html>
```